Chiro Card
Bright Path Chiropractic & Wellness
Project: Chiro Card
Chiro Card -
Creative Brief
Simple
Marcus Hale
Chiropractor
812 Orvale Ave, Suite K Corbin Falls, Tx. 78245
corbinfallsspine@mailvane.com
www.corbinfallsspine.com
Please do not include my email address on the business card.

```html
<!DOCTYPE html>
<html lang="en">
<head>
<meta charset="utf-8">
<title>Bright Path Chiropractic &amp; Wellness – Stationery</title>
<link href="https://fonts.googleapis.com/css2?family=Lato:wght@400;700&display=swap" rel="stylesheet">
<style>
  :root{
    --stage:#4a4c4f;
    --paper:#ffffff;
    --green:#4f9a3a;
    --green-light:#7dbb5c;
    --blue:#1f5f8f;
    --blue-light:#3d86b8;
    --ink:#3b3f44;
    --muted:#8a9096;
    --faint-blue:#dbe6ef;
    --faint-green:#e3efdc;
  }
  *{margin:0;padding:0;box-sizing:border-box}
  html,body{width:1200px;height:346px;overflow:hidden}
  body{background:var(--stage);font-family:'Lato',sans-serif;color:var(--ink);position:relative}
  .sheet{position:absolute;background:var(--paper);overflow:hidden}

  .brand{display:flex;align-items:center;gap:4px}
  .brand-dot{width:9px;height:9px;border-radius:50%;background:var(--green);flex:none}
  .brand-name{font-weight:700;color:var(--green);font-size:9px;line-height:1;white-space:nowrap}
  .brand-tag{font-size:3.6px;color:var(--muted);letter-spacing:.2px;margin-top:1px;white-space:nowrap}

  .mark-area{position:absolute;border-radius:40% 40% 30% 30%;
    background:radial-gradient(ellipse at 50% 40%,var(--faint-blue),var(--faint-green) 60%,transparent 75%)}

  /* business cards */
  .card{width:100px;height:56px}
  .card .brand{position:absolute;left:8px;top:20px}
  .card-back{color:#fff;padding:7px 8px;font-size:3.4px;line-height:1.5}
  .card-back.blue{background:linear-gradient(135deg,var(--blue-light),var(--blue))}
  .card-back.green{background:linear-gradient(135deg,var(--green-light),var(--green))}
  .card-back .person{font-size:5px;font-weight:700;margin-top:8px}
  .card-back .role{font-size:3.6px;margin-bottom:3px}

  /* letterhead */
  .letterhead{width:252px;height:293px;top:19px}
  .letterhead .brand{position:absolute;left:16px;top:16px}
  .letterhead .brand-name{font-size:13px}
  .letterhead .brand-dot{width:12px;height:12px}
  .letterhead .contact{position:absolute;right:14px;top:16px;font-size:3.6px;line-height:1.6;color:var(--muted);text-align:left}
  .letterhead .mark-area{left:86px;top:80px;width:80px;height:120px}
  .letterhead .footer-band{position:absolute;left:0;right:0;bottom:0;height:12px;background:var(--green)}
  .letterhead .footer-line{position:absolute;left:0;right:0;bottom:16px;text-align:center;font-size:3.4px;color:var(--muted)}

  /* envelopes */
  .envelope{width:242px;height:112px}
  .envelope .brand{position:absolute;left:12px;top:12px}
  .envelope .brand-name{font-size:11px}
  .envelope .addr{position:absolute;left:12px;top:30px;font-size:3.4px;color:var(--muted)}
  .envelope .mark-area{right:40px;top:16px;width:48px;height:72px}
  .envelope .strip{position:absolute;left:0;right:0;bottom:0;height:5px;background:var(--green)}

  .envelope-back{width:262px;height:100px}
  .envelope-back svg{position:absolute;inset:0}
  .envelope-back .url{position:absolute;left:0;right:0;top:58px;text-align:center;font-size:3.6px;color:var(--ink)}
</style>
</head>
<body>

<!-- business cards -->
<div class="sheet card" style="left:24px;top:100px">
  <div class="brand"><span class="brand-dot"></span><div><div class="brand-name">BRIGHT PATH</div><div class="brand-tag">Chiropractic &amp; Wellness</div></div></div>
</div>
<div class="sheet card card-back blue" style="left:24px;top:160px">
  <div class="person">Marcus Hale</div>
  <div class="role">Chiropractor</div>
  <div>812 Orvale Ave, Suite K Corbin Falls, Tx. 78245</div>
  <div>www.corbinfallsspine.com</div>
</div>
<div class="sheet card" style="left:24px;top:222px">
  <div class="brand"><span class="brand-dot"></span><div><div class="brand-name">BRIGHT PATH</div><div class="brand-tag">Chiropractic &amp; Wellness</div></div></div>
</div>
<div class="sheet card card-back green" style="left:24px;top:282px;height:56px">
  <div class="person">Marcus Hale</div>
  <div class="role">Chiropractor</div>
  <div>812 Orvale Ave, Suite K Corbin Falls, Tx. 78245</div>
  <div>www.corbinfallsspine.com</div>
</div>

<!-- letterheads -->
<div class="sheet letterhead" style="left:137px">
  <div class="brand"><span class="brand-dot"></span><div><div class="brand-name">BRIGHT PATH</div><div class="brand-tag">Chiropractic &amp; Wellness</div></div></div>
  <div class="contact">Marcus Hale<br>812 Orvale Ave, Suite K<br>Corbin Falls, Tx. 78245<br>corbinfallsspine@mailvane.com</div>
  <div class="mark-area" role="img" aria-label="Faint brand watermark"></div>
  <div class="footer-line">www.corbinfallsspine.com</div>
  <div class="footer-band"></div>
</div>
<div class="sheet letterhead" style="left:402px">
  <div class="mark-area" role="img" aria-label="Faint brand watermark"></div>
  <div class="footer-line">www.corbinfallsspine.com</div>
  <div class="footer-band"></div>
</div>

<!-- front envelopes -->
<div class="sheet envelope" style="left:664px;top:70px">
  <div class="brand"><span class="brand-dot"></span><div><div class="brand-name">BRIGHT PATH</div><div class="brand-tag">Chiropractic &amp; Wellness</div></div></div>
  <div class="addr">812 Orvale Ave, Suite K Corbin Falls, Tx. 78245</div>
  <div class="mark-area" role="img" aria-label="Faint brand watermark"></div>
  <div class="strip"></div>
</div>
<div class="sheet envelope" style="left:664px;top:208px">
  <div class="brand"><span class="brand-dot"></span><div><div class="brand-name">BRIGHT PATH</div><div class="brand-tag">Chiropractic &amp; Wellness</div></div></div>
  <div class="addr">812 Orvale Ave, Suite K Corbin Falls, Tx. 78245</div>
  <div class="mark-area" role="img" aria-label="Faint brand watermark"></div>
  <div class="strip"></div>
</div>

<!-- envelope backs -->
<div class="sheet envelope-back" style="left:918px;top:46px">
  <svg viewBox="0 0 262 100" width="262" height="100">
    <rect width="262" height="100" fill="var(--paper)"/>
    <path d="M0 0 H262 L150 58 Q131 66 112 58 Z" fill="var(--green)"/>
  </svg>
  <div class="url">www.corbinfallsspine.com</div>
</div>
<div class="sheet envelope-back" style="left:918px;top:146px">
  <svg viewBox="0 0 262 100" width="262" height="100">
    <rect width="262" height="100" fill="var(--paper)"/>
    <path d="M0 0 H262 L150 58 Q131 66 112 58 Z" fill="var(--blue)"/>
  </svg>
  <div class="url">www.corbinfallsspine.com</div>
</div>
<div class="sheet envelope-back" style="left:918px;top:246px;height:94px">
  <svg viewBox="0 0 262 94" width="262" height="94">
    <rect width="262" height="94" fill="var(--paper)"/>
    <path d="M0 0 L131 50 L262 0" fill="none" stroke="#c9cdd1" stroke-width="1"/>
    <path d="M0 94 L110 42 M262 94 L152 42" fill="none" stroke="#dde0e3" stroke-width="1"/>
  </svg>
</div>

</body>
</html>
```